Flenzo Thumbnail for Educational Video About KR9

Please design a bespoke thumbnail for a Flenzo video with the following title:
"Nobody Expected What Came Over That Ridge"
The video is about the battle for Castle Brunok, which was a small battle that happened during KR9, in which the Germans fought against themselves for control of Castle Brunok.
The thumbnail should be 1920x1080 pixels

```html
<!DOCTYPE html>
<html lang="en">
<head>
<meta charset="utf-8">
<title>Flenzo – Nobody Expected What Came Over That Ridge</title>
<link href="https://fonts.googleapis.com/css2?family=Montserrat:wght@700;800&display=swap" rel="stylesheet">
<style>
  :root {
    --bg: #000000;
    --ink: #ffffff;
    --ink-dark: #000000;
    --highlight: #fff200;
    --scene-light: #8a8797;
    --scene-mid: #4a3c4f;
    --scene-dark: #1b161d;
  }
  html, body {
    margin: 0;
    padding: 0;
    width: 1200px;
    height: 675px;
    overflow: hidden;
    background: var(--bg);
  }
  .thumbnail {
    position: relative;
    width: 1200px;
    height: 675px;
    background: var(--bg);
    overflow: hidden;
    font-family: "Montserrat", sans-serif;
  }
  .scene-art {
    position: absolute;
    left: 0;
    top: 0;
    width: 340px;
    height: 675px;
    background:
      linear-gradient(to right, rgba(0,0,0,0) 55%, var(--bg) 100%),
      linear-gradient(to bottom, var(--scene-light) 0%, var(--scene-mid) 35%, var(--scene-dark) 75%, var(--bg) 100%);
  }
  .kicker {
    position: absolute;
    left: 12px;
    top: 78px;
    margin: 0;
    font-weight: 800;
    font-size: 44px;
    line-height: 1;
    color: var(--ink);
    -webkit-text-stroke: 8px var(--ink-dark);
    paint-order: stroke fill;
    text-transform: uppercase;
    white-space: nowrap;
    transform: rotate(-20deg);
    transform-origin: left top;
  }
  .kicker-line {
    display: block;
  }
  .headline {
    margin: 0;
    font-weight: 700;
    text-transform: uppercase;
    white-space: nowrap;
  }
  .headline-line {
    position: absolute;
    left: 202px;
    font-size: 130px;
    letter-spacing: -2px;
    color: var(--ink);
  }
  .headline-line--highlight {
    top: 104px;
    height: 170px;
    line-height: 170px;
    padding: 0 26px 0 22px;
    background: var(--highlight);
    color: var(--ink-dark);
  }
  .headline-line--plain {
    height: 140px;
    line-height: 140px;
    padding-left: 22px;
  }
  .headline-line--second { top: 276px; }
  .headline-line--third { top: 430px; }
</style>
</head>
<body>
  <main class="thumbnail">
    <div class="scene-art" role="img" aria-label="Dark castle gateway at night with an army tank parked under the stone arch"></div>
    <p class="kicker">
      <span class="kicker-line">Nobody</span>
      <span class="kicker-line">Expected</span>
    </p>
    <h1 class="headline">
      <span class="headline-line headline-line--highlight">What Came</span>
      <span class="headline-line headline-line--plain headline-line--second">Over That</span>
      <span class="headline-line headline-line--plain headline-line--third">Ridge!</span>
    </h1>
  </main>
</body>
</html>
```